Migration Lawyers

Company: Dunstan & Co Lawyers & Migration Agents

Name: Graham Dunstan BEc, LLB
Address: Level 18, 72 Hollis Street
Sydney, NSW, Australia 2000

Ph: +61 2 9384 5207
M: 0428316540
E: graham@permitpath-example.org.au
W: www.permitpath-example.org.au

Target Market(s)

Migration Clients

Industry/Entity Type

It Company

Font styles to use
Script

Requirements
Must have
• Logo
Should not have
• Please scale the format to the printing size attached

```html
<!DOCTYPE html>
<html lang="en">
<head>
<meta charset="utf-8">
<title>Dunstan &amp; Co — Business Card</title>
<link rel="stylesheet" href="https://fonts.googleapis.com/css2?family=Parisienne&family=Libre+Baskerville:wght@400;700&display=swap">
<style>
  :root {
    --stage: #e9e7e4;
    --card-light: #ffffff;
    --card-dark: #0b0b0b;
    --ink: #141414;
    --ink-soft: #3a3a3a;
    --ink-light: #f2f2f2;
    --ink-muted: #bdbdbd;
    --art-warm: #c98a62;
    --art-gold: #d9c79a;
  }
  * { margin: 0; padding: 0; box-sizing: border-box; }
  html, body { width: 1200px; height: 787px; overflow: hidden; }
  body {
    background: var(--stage);
    display: flex;
    align-items: center;
    justify-content: center;
    gap: 60px;
  }
  .card {
    position: relative;
    width: 520px;
    height: 318px;
    border-radius: 2px;
    box-shadow: 0 6px 18px rgba(0,0,0,0.15);
    overflow: hidden;
  }

  /* Front */
  .card--front { background: var(--card-light); color: var(--ink); }
  .card__art {
    position: absolute;
    left: 170px; top: 38px;
    width: 260px; height: 200px;
    border-radius: 8px;
    background: radial-gradient(ellipse at 60% 65%, var(--art-warm) 0%, var(--art-gold) 45%, rgba(255,255,255,0) 75%);
    opacity: 0.22;
  }
  .holder {
    position: absolute;
    left: 100px; top: 28px;
  }
  .holder__name {
    font-family: "Parisienne", cursive;
    font-size: 30px;
    line-height: 1;
    font-weight: 400;
    letter-spacing: 0.5px;
  }
  .holder__title {
    font-family: "Parisienne", cursive;
    font-size: 15px;
    color: var(--ink-soft);
    margin-left: 2px;
  }
  .address, .phones {
    position: absolute;
    font-family: "Parisienne", cursive;
    font-size: 21px;
    line-height: 1.12;
  }
  .address { left: 92px; top: 104px; }
  .phones { left: 82px; top: 168px; }
  .email {
    position: absolute;
    left: 72px; top: 240px;
    font-family: "Parisienne", cursive;
    font-size: 19px;
  }
  .brand {
    position: absolute;
    right: 26px; top: 22px;
    width: 120px;
    text-align: center;
    font-family: "Libre Baskerville", serif;
  }
  .brand__dot {
    display: block;
    width: 38px; height: 38px;
    margin: 0 auto 6px;
    border: 2px solid var(--ink);
    border-radius: 50%;
  }
  .brand__name { font-size: 13px; font-weight: 700; line-height: 1.2; }
  .brand__tag { font-size: 6.5px; font-weight: 700; line-height: 1.3; }

  /* Back */
  .card--back {
    background: var(--card-dark);
    color: var(--ink-light);
    display: flex;
    flex-direction: column;
    align-items: center;
    justify-content: center;
    font-family: "Libre Baskerville", serif;
  }
  .back__ring {
    width: 110px; height: 110px;
    border: 3px solid var(--ink-light);
    border-radius: 50%;
    margin-bottom: 18px;
  }
  .back__name { font-size: 26px; font-weight: 700; }
  .back__tag { font-size: 12px; font-weight: 700; color: var(--ink-muted); margin-top: 4px; }
  .back__web {
    position: absolute;
    bottom: 22px; right: 24px;
    font-family: "Parisienne", cursive;
    font-size: 18px;
    color: var(--ink-light);
  }
</style>
</head>
<body>
  <section class="card card--front">
    <div class="card__art" role="img" aria-label="Faint image of scales of justice and a wooden gavel"></div>
    <div class="holder">
      <div class="holder__name">Graham Dunstan</div>
      <div class="holder__title">BEc, LLB</div>
    </div>
    <div class="address">
      <div>Level 18, 72 Hollis Street</div>
      <div>Australia, Sydney, NSW, 2000</div>
    </div>
    <div class="phones">
      <div>Tel: +61 2 9384 5207</div>
      <div>Mob: 0428316540</div>
    </div>
    <div class="email">graham@permitpath-example.org.au</div>
    <div class="brand">
      <span class="brand__dot"></span>
      <div class="brand__name">Dunstan &amp; Co</div>
      <div class="brand__tag">Lawyers &amp; Migration Agents</div>
    </div>
  </section>

  <section class="card card--back">
    <div class="back__ring"></div>
    <div class="back__name">Dunstan &amp; Co</div>
    <div class="back__tag">Lawyers &amp; Migration Agents</div>
    <div class="back__web">www.permitpath-example.org.au</div>
  </section>
</body>
</html>
```